Mesh Banner Design for Business Premises

We require the design of a large mesh banner to be installed across the front fence of our warehouse. The banner should prominently feature our existing Trelborn logo and brand colours (yellow, white, and black) and be designed to be highly visible from the road.

The overall aesthetic should be strong, masculine, and industrial, reflecting the nature of the scaffolding and construction industry. The background should be predominantly black, with our branding incorporated in yellow and white for strong contrast and readability.

The banner should clearly communicate the full scope of services we provide, including:

Scaffold Design
Scaffold Engineering
Scaffold Installation / Erection
Scaffold Dismantling

It should also indicate the types of projects and clients we service, including:

Commercial
Industrial
Residential
Civil

The design should feel bold and professional, with a construction-oriented style that aligns with the scaffolding industry. It should be clean, impactful, and easy to read from a distance, ensuring passing traffic can quickly understand our services.

Where possible, subtle industrial or structural design elements (such as scaffold components, steel textures, or linework) may be incorporated into the background to reinforce the industry theme while keeping the layout uncluttered.

The final design will be produced as a large-format mesh banner for outdoor installation, so it should be created with this application and viewing distance in mind.

```html
<!DOCTYPE html>
<html lang="en">
<head>
<meta charset="utf-8">
<title>Trelborn Mesh Banner</title>
<link rel="stylesheet" href="https://fonts.googleapis.com/css2?family=Jost:wght@600;700&family=Questrial&display=swap">
<style>
  :root {
    --backdrop: #bdbdbd;
    --banner-black: #231f20;
    --brand-yellow: #f9b21d;
    --text-white: #ffffff;
  }
  * { margin: 0; padding: 0; box-sizing: border-box; }
  html, body {
    width: 1200px;
    height: 403px;
    overflow: hidden;
    background: var(--backdrop);
  }
  .canvas {
    position: relative;
    width: 1200px;
    height: 403px;
  }
  .banner {
    position: absolute;
    left: 96px;
    top: 69px;
    width: 1009px;
    height: 257px;
    background: var(--banner-black);
  }
  .section-heading {
    position: absolute;
    font-family: "Jost", sans-serif;
    font-weight: 600;
    color: var(--brand-yellow);
    font-size: 19px;
    line-height: 22px;
    text-align: center;
    white-space: nowrap;
  }
  .services-heading { left: 45px; width: 260px; top: 37px; }
  .clients-heading { left: 712px; width: 246px; top: 36px; }

  .tile {
    position: absolute;
    border: 2px solid var(--brand-yellow);
    border-radius: 8px;
    display: flex;
    align-items: center;
    justify-content: center;
    text-align: center;
    font-family: "Questrial", sans-serif;
    color: var(--text-white);
    white-space: nowrap;
  }
  .service-tile { font-size: 16.5px; line-height: 20px; width: 121px; }
  .service-tile.top { top: 75px; height: 75px; }
  .service-tile.bottom { top: 158px; height: 61px; }
  .service-tile.col-a { left: 45px; }
  .service-tile.col-b { left: 186px; }

  .client-tile { font-size: 20px; width: 132px; height: 53px; }
  .client-tile.top { top: 99px; }
  .client-tile.bottom { top: 166px; }
  .client-tile.col-a { left: 693px; }
  .client-tile.col-b { left: 846px; }

  .divider {
    position: absolute;
    top: 43px;
    width: 2px;
    height: 182px;
    background: var(--brand-yellow);
  }
  .divider.left { left: 345px; }
  .divider.right { left: 669px; }

  .brand-block {
    position: absolute;
    left: 357px;
    top: 48px;
    width: 302px;
    display: flex;
    flex-direction: column;
    align-items: center;
    text-align: center;
  }
  .brand-mark {
    display: block;
  }
  .brand-name {
    margin-top: 14px;
    font-family: "Questrial", sans-serif;
    color: var(--text-white);
    font-size: 19px;
    letter-spacing: 16px;
    padding-left: 16px;
    line-height: 20px;
    white-space: nowrap;
  }
  .hotline {
    margin-top: 10px;
    font-family: "Jost", sans-serif;
    font-weight: 700;
    color: var(--text-white);
    font-size: 32px;
    line-height: 36px;
    white-space: nowrap;
  }
</style>
</head>
<body>
<div class="canvas">
  <section class="banner">
    <h2 class="section-heading services-heading">Services we provide</h2>
    <div class="tile service-tile top col-a">Scaffold<br>Design</div>
    <div class="tile service-tile top col-b">Scaffold<br>Installation /<br>Erection</div>
    <div class="tile service-tile bottom col-a">Scaffold<br>Engineering</div>
    <div class="tile service-tile bottom col-b">Scaffold<br>Dismantling</div>

    <div class="divider left"></div>

    <div class="brand-block">
      <svg class="brand-mark" width="84" height="84" viewBox="0 0 84 84" aria-hidden="true">
        <circle cx="42" cy="42" r="39" fill="none" stroke="var(--brand-yellow)" stroke-width="3"/>
      </svg>
      <div class="brand-name">TRELBORN</div>
      <div class="hotline">1300 6 FRAME</div>
    </div>

    <div class="divider right"></div>

    <h2 class="section-heading clients-heading">Types of projects<br>and clients we service</h2>
    <div class="tile client-tile top col-a">Commercial</div>
    <div class="tile client-tile top col-b">Residential</div>
    <div class="tile client-tile bottom col-a">Industrial</div>
    <div class="tile client-tile bottom col-b">Civil</div>
  </section>
</div>
</body>
</html>
```